Health & Fitness Author & Public Speaker Needs Visually Stunning Web Redesign!

It's time for a redesign of the home page for Beatrix Holloway's "Bright Fork Kitchen" website (www.brightforkkitchen.example). We have a VERY clear idea of what we want, so it really won't take a talented designer long to bring it to life.
The website itself is used to promote & sell her range of health & nutrition programs to a female audience, primarily aged 24 - 35 working in professional or semi professional occupations.
For a VERY comprehensive outline of exactly what we are after, please see the following attached files:
(1) 'Website - WireFrame' (layout, content/copy, visual design style we want along with the desired color scheme)
(2) 'Website - Style Guide' (these are the colours, and overall feel we want)
PLEASE REVIEW THIS IN FULL - THEY WILL GIVE YOU A VERY CLEAR IDEA OF WHAT WE WANT.
Most of the files you need are attached, but for more photos that you can use (of Beatrix, her programs, and food/meals) can be found at these URL's:
BEATRIX (profile photos):
https://www.filevault.example/s/k3m9p2x7q1/AbCdEf1234
ECOVERS
- Bright Fork Kitchen Guide (ebook): https://www.filevault.example/s/r8t4w6y2n5/GhIjKl5678
- 6 Week Total Momentum Course (ecourse): https://www.filevault.example/s/u1v5z9c3b7/MnOpQr9012
- E-Magazine Issues:
https://www.filevault.example/s/d2f6h8j4l0/StUvWx3456
STOCK IMAGES:
https://www.filevault.example/s/g7k1m5n9p3/YzAbCd7890
As we will need to revamp our existing Facebook page & other printed material, there may be the potential for further work for the successful designer in the future.
Thanks & Good Luck!
Desmond Farrow
Marketing & Business Development Manager
Bright Fork Kitchen

```html
<!DOCTYPE html>
<html lang="en">
<head>
<meta charset="utf-8">
<title>Bright Fork Kitchen</title>
<link rel="stylesheet" href="https://fonts.googleapis.com/css2?family=Amatic+SC:wght@700&family=Jost:wght@500;600&family=Open+Sans:wght@400;600;700&display=swap">
<style>
  :root{
    --navy:#1f3b6b;
    --pink:#ee1650;
    --green:#13a287;
    --text:#6f6f6f;
    --white:#ffffff;
    --bg-a:#fbe6fb;
    --bg-b:#e4f6fd;
  }
  *{margin:0;padding:0;box-sizing:border-box}
  html,body{width:1200px;height:926px;overflow:hidden}
  body{
    position:relative;
    background:linear-gradient(120deg,var(--bg-a) 0%,#eee9fb 40%,var(--bg-b) 100%);
    font-family:"Open Sans",sans-serif;
  }
  .page{position:absolute;left:74px;top:66px;width:1044px;height:860px;background:var(--white);overflow:hidden}
  .page-fade{position:absolute;left:0;right:0;bottom:0;height:110px;
    background:linear-gradient(to bottom,rgba(255,255,255,0),rgba(246,236,246,.95))}

  .brand{position:absolute;left:76px;top:34px;display:flex;align-items:center;gap:8px;
    font-family:"Jost",sans-serif;font-weight:600;font-size:20px;color:var(--pink)}
  .brand-dot{width:12px;height:12px;border-radius:50%;background:var(--pink)}

  .nav{position:absolute;right:63px;top:29px;display:flex;align-items:center;gap:26px;
    font-family:"Jost",sans-serif;font-weight:600;font-size:16px;letter-spacing:.3px;color:var(--green)}
  .nav-shop{background:var(--pink);color:var(--white);padding:4px 9px;border-radius:5px;margin-left:-17px}

  .hero{position:absolute;left:0;top:80px;width:1044px;height:340px;background:var(--navy)}
  .hero-title{position:absolute;left:120px;top:86px;width:590px;text-align:center;
    font-family:"Amatic SC",cursive;font-weight:700;font-size:70px;line-height:66px;color:var(--white)}
  .hero-photo{position:absolute;left:753px;top:8px;width:145px;height:332px;border-radius:70px 70px 0 0;
    background:linear-gradient(to bottom,#3a2a28 0%,#e8ecf4 30%,#eef1f6 55%,#2c3f66 70%,#223459 100%)}

  .signup{position:absolute;left:0;top:420px;width:1044px;height:108px;background:var(--pink)}
  .signup-copy{position:absolute;right:616px;top:18px;text-align:right;color:var(--white)}
  .signup-title{font-weight:700;font-size:20px;line-height:27px}
  .signup-text{font-size:15px;line-height:22px}
  .field{position:absolute;top:36px;width:177px;height:37px;border-radius:5px;background:var(--white);
    font-family:"Jost",sans-serif;font-weight:500;font-size:17px;color:#777;padding:7px 11px;letter-spacing:.3px}
  .field-name{left:455px}
  .field-email{left:653px}
  .signup-button{position:absolute;left:851px;top:36px;width:123px;height:37px;border-radius:4px;
    background:var(--green);color:var(--white);font-family:"Jost",sans-serif;font-weight:600;
    font-size:17px;text-align:center;line-height:37px}

  .intro{position:absolute;left:69px;top:554px;width:620px}
  .intro-title{font-family:"Jost",sans-serif;font-weight:500;font-size:19px;line-height:26px;color:var(--green);letter-spacing:.2px}
  .intro-text{margin-top:23px;font-size:15.5px;line-height:22.5px;color:var(--text)}

  .press{position:absolute;left:718px;top:557px;width:220px}
  .press-label{font-size:14px;color:var(--text);letter-spacing:.2px}
  .press-badge{position:absolute;left:20px;border-radius:3px}
  .badge-pink{top:32px;width:186px;height:62px;background:var(--pink)}
  .badge-dark{top:107px;width:186px;height:28px;background:#1f1f1f}
  .badge-gold{top:146px;width:186px;height:38px;background:#9c7a3c}
</style>
</head>
<body>
  <main class="page">
    <header>
      <div class="brand"><span class="brand-dot"></span>Bright Fork Kitchen</div>
      <nav class="nav">
        <span>ABOUT BEATRIX</span>
        <span>THE MAGAZINE</span>
        <span>BLOG &amp; VIDEOS</span>
        <span class="nav-shop">SHOP</span>
      </nav>
    </header>

    <section class="hero">
      <h1 class="hero-title">You don’t need another diet<br>to get the body you want!</h1>
      <div class="hero-photo" role="img" aria-label="Photo of Beatrix in a white tee and jeans holding a slice of watermelon"></div>
    </section>

    <section class="signup">
      <div class="signup-copy">
        <p class="signup-title">Get my FREE monthly E-Magazine</p>
        <p class="signup-text">With delicious recipes,inspirational articles, workouts<br>&amp; expert wellness tips that actually work! Yup FREE!</p>
      </div>
      <div class="field field-name">FIRST NAME</div>
      <div class="field field-email">EMAIL</div>
      <div class="signup-button">YES PLEASE!</div>
    </section>

    <section class="intro">
      <h2 class="intro-title">Want a Body You’re Proud Of AND a Healthy Lifestyle You Love?<br>Then You Don’t Need Another Diet!</h2>
      <p class="intro-text">Hey there I’m Beatrix. I help smart, savvy, driven women just like you to slim down so you can not only rock your outfit but you can enjoy a lifestyle to match.&nbsp; As hard as it might be for you to believe right now, I’ll teach you how to have this in a way that’s easier, and heaps more enjoyable than you’d ever thought possible – it’s time to kiss guilt and deprivation goodbye!</p>
    </section>

    <aside class="press">
      <p class="press-label">ALREADY DISCOVERED BY:</p>
      <div class="press-badge badge-pink"></div>
      <div class="press-badge badge-dark"></div>
      <div class="press-badge badge-gold"></div>
    </aside>

    <div class="page-fade"></div>
  </main>
</body>
</html>
```